postcard design for moving company

Bramwell  Movers and Storage -moving company , we send postcards to potential clients that have their houses for sale. Must be a postard that is easy to read , where you can notice some deals, reason not to throw the card to junk.
family owned and operated company.
Free estimate
Flat Rate , license and insured, then we must put the zindle and vork 5 stars.
coupons:
$50 Off for all long distance moving
1 month Free Storage for out of state moves.
5% Off for seniors nd veterans.

```html
<!DOCTYPE html>
<html lang="en">
<head>
<meta charset="utf-8">
<title>Bramwell Movers and Storage – Postcard</title>
<link rel="stylesheet" href="https://fonts.googleapis.com/css2?family=Poppins:wght@400;500;600;700;800&display=swap">
<style>
:root{
  --red:#e04a4b;
  --red-deep:#c93a3c;
  --ink:#3a2e3d;
  --ink-soft:#4a3f4d;
  --paper:#ffffff;
  --backdrop:#cacaca;
  --line:#d9d9d9;
  --gold:#f7b50c;
  --muted:#9a9a9a;
}
*{box-sizing:border-box;margin:0;padding:0}
html,body{width:750px;height:1200px;overflow:hidden}
body{background:var(--backdrop);font-family:'Poppins',sans-serif;color:var(--ink);position:relative}
.card{position:absolute;left:35px;width:680px;height:452px;background:var(--paper);overflow:hidden;box-shadow:0 6px 14px rgba(0,0,0,.22)}
.card--front{top:112px}
.card--back{top:628px}
.abs{position:absolute}

/* brand */
.brand{position:absolute;font-family:'Poppins',sans-serif;font-weight:600;color:var(--red);line-height:1;letter-spacing:-.5px}
.brand small{display:block;font-size:.55em;text-align:right;margin-top:2px}

/* front */
.headline{left:41px;top:82px;font-weight:800;font-size:38px;line-height:39px;letter-spacing:-.5px;color:var(--ink)}
.headline .hl-red{color:var(--red)}
.ribbon{left:41px;top:214px;width:212px;height:20px;background:var(--red);color:#fff;font-size:11px;font-weight:500;letter-spacing:4.2px;line-height:20px;padding-left:10px}
.ribbon-tip{left:253px;top:214px}
.perks{left:41px;top:250px;display:flex}
.perk{width:94px;text-align:center;font-size:9.5px;font-weight:600;line-height:12px;border-right:1px solid var(--line);padding-top:2px}
.perk:last-child{border-right:none;width:80px}
.perk svg{display:block;margin:0 auto 4px}
.storage{left:41px;top:318px;border-right:1px solid var(--ink);border-top:1px solid var(--ink);border-top-right-radius:6px;padding-right:8px}
.storage .big{font-size:22px;font-weight:800;color:var(--red);line-height:26px}
.storage .big b{color:var(--ink);font-weight:800;margin-right:4px}
.storage .big span{color:var(--ink);font-size:15px;margin-left:4px}
.storage .sub{font-size:9.5px;letter-spacing:3.4px;font-weight:500}
.photo{background:linear-gradient(135deg,#e6e6e6 0%,#bdbdbd 30%,#3a3a3a 55%,#262626 100%)}
.photo--truck{left:300px;top:0;width:380px;height:442px;clip-path:polygon(22% 0,100% 0,100% 100%,0 100%,0 55%)}
.burst{left:262px;top:30px;width:136px;height:136px;border-radius:50%;background:var(--red);border:3px dotted #fff;outline:4px solid var(--red);color:#fff;text-align:center;transform:rotate(-8deg);padding-top:24px}
.burst .amt{font-size:40px;font-weight:800;line-height:40px}
.burst .amt sup{font-size:18px;vertical-align:top}
.burst .amt em{font-style:normal;font-size:20px}
.burst .txt{font-size:12px;line-height:13px;font-weight:500}
.bar{left:0;top:391px;width:336px;height:50px;background:var(--ink);border-top-right-radius:30px 50px;color:#fff;display:flex;align-items:center;padding-left:43px;z-index:2}
.bar .lbl{font-size:11px;font-weight:600;margin-right:4px}
.bar .num{font-size:21px;font-weight:700;letter-spacing:.3px;margin-left:3px}
.strip{left:0;top:441px;width:680px;height:11px;background:var(--red)}
.deal-band{left:320px;top:395px;width:360px;height:50px;background:var(--red);color:#fff;padding:6px 0 0 12px;border-top-left-radius:20px}
.deal-band .t1{font-size:18px;font-weight:800;line-height:20px}
.deal-band .t1 span{font-weight:400}
.deal-band .t2{font-size:10px;font-weight:600}

/* back */
.rating-copy{left:40px;top:38px;font-size:15px;line-height:19px;font-weight:500}
.rating-copy b{font-weight:700}
.rating-copy .z{color:#2f6fe4;font-weight:700}
.rating-copy .v{color:var(--red);font-weight:700}
.rating-divider{left:150px;top:40px;width:1px;height:60px;background:var(--line)}
.badge{width:26px;height:26px;border-radius:6px}
.badge--a{left:164px;top:42px;background:#eef1f6;border:1px solid #d7dce6}
.badge--b{left:164px;top:72px;background:var(--red)}
.score{left:198px;top:30px;font-size:50px;font-weight:800;line-height:56px}
.stars{left:199px;top:84px}
.coupon{left:40px;width:173px;height:80px;display:flex}
.coupon .stub{width:46px;background:var(--ink);border-radius:10px 0 0 10px;color:#fff;display:flex;align-items:center;justify-content:center;border-right:2px dashed #fff}
.coupon .stub span{transform:rotate(-90deg);white-space:nowrap;font-weight:800;font-size:13px}
.coupon .stub span i{font-style:normal;font-size:8px;font-weight:600}
.coupon .body{flex:1;background:var(--red);border-radius:0 10px 10px 0;color:#fff;padding:8px 0 0 16px;box-shadow:0 3px 4px rgba(0,0,0,.15)}
.coupon .row{display:flex;align-items:center}
.coupon .amt{font-size:20px;font-weight:700;line-height:19px}
.coupon .amt sup{font-size:11px;vertical-align:top}
.coupon .note{font-size:8px;font-weight:600;line-height:9px;margin-left:6px}
.coupon .note span{font-weight:400}
.coupon .tag{font-size:5.5px;letter-spacing:2.4px;margin-top:7px;opacity:.9}
.coupon .month{font-size:19px;font-weight:700;line-height:19px}
.coupon .month-sub{font-size:10px;font-weight:800;line-height:11px}
.coupon .month-note{font-size:7.5px}
.c1{top:113px}.c2{top:200px}.c3{top:287px}
.photo--mover{left:213px;top:114px;width:150px;height:280px;background:linear-gradient(180deg,#eaeaea 0%,#3d3b45 35%,#2d2b33 70%,#b89778 100%);border-radius:40px 40px 0 0}
.stamp{left:571px;top:45px;width:67px;height:84px;border:1px solid #c7c7c7}
.addr{left:364px;width:276px;height:1px;background:var(--line)}
.bar--back .num{font-size:21px}
.family-band{left:320px;top:397px;width:165px;height:55px;background:var(--red);color:#fff;font-size:10px;font-weight:600;line-height:12px;padding:10px 0 0 14px;clip-path:polygon(0 0,80% 0,100% 100%,0 100%);border-top-left-radius:20px}
</style>
</head>
<body>

<!-- Front -->
<section class="card card--front" aria-label="Postcard front">
  <div class="abs photo photo--truck" role="img" aria-label="Photo of a branded moving truck with a mover carrying a roll of packing wrap"></div>

  <div class="brand" style="left:41px;top:40px;font-size:21px">bramwell movers<small>&amp; storage</small></div>

  <h1 class="abs headline"><span class="hl-red">BRAMWELL</span><br>MOVERS &amp;<br>STORAGE</h1>
  <div class="abs ribbon">MOVING COMPANY</div>
  <svg class="abs ribbon-tip" width="10" height="20" viewBox="0 0 10 20"><polygon points="0,0 10,20 0,20" fill="var(--ink)"/></svg>

  <div class="abs perks">
    <div class="perk">
      <svg width="30" height="26" viewBox="0 0 30 26" fill="var(--ink)"><circle cx="15" cy="4" r="3.5" fill="var(--red)"/><circle cx="8" cy="10" r="3.2"/><circle cx="22" cy="10" r="3.2"/><circle cx="15" cy="13" r="2.6"/><path d="M2 26v-6c0-3 3-5 6-5s6 2 6 5v6zM16 26v-6c0-3 3-5 6-5s6 2 6 5v6z"/><path d="M11 26v-4c0-2 2-3 4-3s4 1 4 3v4z" fill="#fff" stroke="var(--ink)"/></svg>
      Family owned<br>&amp; operated
    </div>
    <div class="perk">
      <svg width="30" height="26" viewBox="0 0 30 26"><rect x="7" y="1" width="15" height="22" rx="2" fill="var(--ink)"/><rect x="9.5" y="3.5" width="10" height="5" fill="#fff"/><g fill="#fff"><rect x="9.5" y="11" width="2.5" height="2.5"/><rect x="13.5" y="11" width="2.5" height="2.5"/><rect x="17" y="11" width="2.5" height="2.5"/><rect x="9.5" y="15" width="2.5" height="2.5"/><rect x="13.5" y="15" width="2.5" height="2.5"/></g><circle cx="23" cy="20" r="5.5" fill="var(--red)"/><text x="23" y="23" font-size="8" font-weight="700" fill="#fff" text-anchor="middle" font-family="Poppins,sans-serif">$</text></svg>
      Free estimate
    </div>
    <div class="perk">
      <svg width="30" height="26" viewBox="0 0 30 26"><circle cx="17" cy="7" r="6" fill="var(--red)"/><text x="17" y="10.5" font-size="9" font-weight="700" fill="#fff" text-anchor="middle" font-family="Poppins,sans-serif">$</text><path d="M4 17h8l6 2 6-3 2 2-8 5H4z" fill="var(--ink)"/><rect x="1" y="16" width="3" height="9" fill="var(--ink)"/></svg>
      Flat Rate
    </div>
  </div>

  <div class="abs storage">
    <div class="big"><b>1</b>MONTH<span>Free Storage</span></div>
    <div class="sub">FOR OUT OF STATE MOVES</div>
  </div>

  <div class="abs burst">
    <div class="amt"><sup>$</sup>50<em>OFF</em></div>
    <div class="txt">for all long<br>distance<br>moving</div>
  </div>

  <div class="abs deal-band">
    <div class="t1">5% OFF <span>FOR</span></div>
    <div class="t2">SENIORS &amp; VETERANS</div>
  </div>
  <div class="abs bar">
    <span class="lbl">Call us</span>
    <svg width="18" height="18" viewBox="0 0 18 18"><circle cx="9" cy="9" r="8" fill="var(--red)"/><path d="M6 4.5l1.6 2.2-1 1.2c.6 1.4 1.6 2.4 3 3l1.2-1 2.2 1.6-.9 1.8c-3.4-.3-6.3-3.2-6.6-6.6z" fill="#fff"/></svg>
    <span class="num">555 014 2277</span>
  </div>
  <div class="abs strip"></div>
</section>

<!-- Back -->
<section class="card card--back" aria-label="Postcard back">
  <p class="abs rating-copy"><b>5 star</b> rating<br>on <span class="z">zindle</span><br>and <span class="v">vork</span></p>
  <div class="abs rating-divider"></div>
  <div class="abs badge badge--a"></div>
  <div class="abs badge badge--b"></div>
  <div class="abs score">5.0</div>
  <svg class="abs stars" width="80" height="14" viewBox="0 0 80 14" fill="var(--gold)">
    <defs><polygon id="star" points="7,0 8.7,4.8 13.8,5 9.8,8.1 11.2,13 7,10.2 2.8,13 4.2,8.1 0.2,5 5.3,4.8"/></defs>
    <use href="#star" x="0"/><use href="#star" x="16"/><use href="#star" x="32"/><use href="#star" x="48"/><use href="#star" x="64"/>
  </svg>

  <div class="brand" style="left:364px;top:44px;font-size:17px">bramwell movers<small style="text-align:left;margin-left:66px">&amp; storage</small></div>

  <div class="abs stamp"></div>
  <div class="abs addr" style="top:184px"></div>
  <div class="abs addr" style="top:232px"></div>
  <div class="abs addr" style="top:279px"></div>
  <div class="abs addr" style="top:326px"></div>

  <div class="abs photo photo--mover" role="img" aria-label="Photo of a cheerful mover giving a thumbs up beside stacked cardboard boxes"></div>

  <div class="abs coupon c1">
    <div class="stub"><span>$50 <i>OFF</i></span></div>
    <div class="body">
      <div class="row"><div class="amt"><sup>$</sup>50<br>OFF</div><div class="note"><span>FOR ALL</span><br>LONG<br>DISTANCE<br>MOVING</div></div>
      <div class="tag">DISCOUNT COUPON</div>
    </div>
  </div>
  <div class="abs coupon c2">
    <div class="stub"><span>1 MONTH</span></div>
    <div class="body" style="padding-left:12px">
      <div class="month">1 MONTH</div>
      <div class="month-sub">FREE STORAGE</div>
      <div class="month-note">For out of state moves</div>
      <div class="tag" style="margin-top:5px">DISCOUNT COUPON</div>
    </div>
  </div>
  <div class="abs coupon c3">
    <div class="stub"><span>$5 <i>OFF</i></span></div>
    <div class="body">
      <div class="row"><div class="amt"><sup>$</sup>5<br>OFF</div><div class="note"><span>FOR</span><br>SENIORS &amp;<br>VETERANS</div></div>
      <div class="tag">DISCOUNT COUPON</div>
    </div>
  </div>

  <div class="abs family-band">FAMILY OWNED &amp;<br>OPERATED COMPANY</div>
  <div class="abs bar bar--back">
    <span class="lbl">Call us</span>
    <svg width="18" height="18" viewBox="0 0 18 18"><circle cx="9" cy="9" r="8" fill="var(--red)"/><path d="M6 4.5l1.6 2.2-1 1.2c.6 1.4 1.6 2.4 3 3l1.2-1 2.2 1.6-.9 1.8c-3.4-.3-6.3-3.2-6.6-6.6z" fill="#fff"/></svg>
    <span class="num">555 014 2277</span>
  </div>
  <div class="abs strip" style="width:485px"></div>
</section>

</body>
</html>
```